Price Calculator as Responsive Web App to support Sales People

We need to build a simple micro web app to support sales people in making quotes. We already have a backend that can take a number of parameters and create a quote. We need put a responsive web app on top of this so that our people on the road can easily do their price simulations.

We need two pages. One for the input and another for the results. No menus, navigations, etc. It is 6 different inputs as shown with boxes in the sketch. They don't need to be boxed, but some of them have a bit of instruction text that clearly need to belong to the input.

This needs to be responsive, but first and foremost designed for smartphones. I have included a background gradient that we would like to use -- or a variant of it. We expect this to be delivered as HTML/CSS + images so that we can quickly write a few pieces of JavaScript ourselves to wire it up to our price simulator.

Industry/Entity Type

Information Technology

Coding

Coded - Design and coding required

Number of Pages Required

2 page

Font styles to use
Sans Serif

Requirements
Must have
• Responsive design
• Easy to wire up JavaScript to the HTML/CSS
Nice to have
• Some quick way to pick number of months. +/- buttons to add remove a year or 3 months. Same thing with number of items. Add 10 or 5 quickly.
• Maybe some parallax effect while scrolling as long as it is not distracting.
Should not have
• Toolbars, Menus, Navigations, Banners, etc. This is just a single micro app.

```html
<!DOCTYPE html>
<html lang="en">
<head>
<meta charset="utf-8">
<title>Calculate Your Order</title>
<link href="https://fonts.googleapis.com/css2?family=Open+Sans:wght@400;600;700&display=swap" rel="stylesheet">
<style>
  :root {
    --bg-top: #013a69;
    --bg-mid: #012540;
    --bg-bottom: #001a2d;
    --card: #ffffff;
    --ink: #1e1e1e;
    --muted: #6b6b6b;
    --line: #e3e3e3;
    --navy: #053a65;
    --blue: #1e7be0;
    --red: #d81f26;
    --green: #4d9e12;
  }
  * { box-sizing: border-box; margin: 0; padding: 0; }
  html, body { width: 1200px; height: 833px; overflow: hidden; }
  body {
    font-family: "Open Sans", sans-serif;
    color: var(--ink);
    background: linear-gradient(to bottom, var(--bg-top) 0, var(--bg-mid) 180px, var(--bg-bottom) 833px);
    position: relative;
  }
  .order-card {
    position: absolute; left: 196px; top: 50px; width: 808px; height: 800px;
    background: var(--card);
  }
  .card-header {
    position: absolute; left: 0; top: 0; width: 808px; height: 140px;
    border-bottom: 1px solid var(--line);
  }
  .page-title {
    position: absolute; left: 84px; top: 50px;
    font-size: 32px; font-weight: 700; letter-spacing: 0.3px; line-height: 42px;
  }
  .help-center {
    position: absolute; left: 476px; top: 0; width: 332px; height: 140px;
    border-left: 1px solid var(--line); padding: 16px 0 0 24px;
  }
  .help-heading {
    display: flex; align-items: center; gap: 7px;
    font-size: 10.5px; font-weight: 700; color: var(--blue); letter-spacing: 0.6px;
  }
  .help-text { margin-top: 17px; font-size: 11px; line-height: 15px; color: var(--muted); width: 220px; }
  .help-contact { margin-top: 15px; font-size: 11px; color: var(--ink); }

  .step { position: absolute; left: 0; width: 808px; }
  .step-number {
    position: absolute; left: 96px; width: 33px; height: 33px; border-radius: 50%;
    background: var(--navy); color: #fff; font-size: 20px; font-weight: 400;
    display: flex; align-items: center; justify-content: center;
  }
  .step-title { position: absolute; left: 166px; font-size: 21.5px; font-weight: 600; letter-spacing: 0.3px; line-height: 28px; }
  .step-desc { position: absolute; left: 166px; font-size: 11px; color: var(--muted); letter-spacing: 0.3px; }
  .stepper { position: absolute; left: 0; height: 38px; width: 808px; }
  .step-btn {
    position: absolute; top: 0; width: 38px; height: 38px; border-radius: 50%;
    background: #fff; font-family: inherit; font-size: 10.5px; font-weight: 700;
    display: flex; align-items: center; justify-content: center;
  }
  .step-btn.minus { border: 1px solid var(--red); color: var(--red); }
  .step-btn.plus { border: 1px solid var(--green); color: var(--green); }
  .value-pill {
    position: absolute; left: 334px; top: 0; width: 141px; height: 37px;
    border: 1px solid var(--blue); border-radius: 19px;
    display: flex; align-items: center;
  }
  .value-number { width: 78px; text-align: center; font-size: 20px; font-weight: 600; color: var(--blue); }
  .value-unit { font-size: 11px; letter-spacing: 0.6px; color: var(--ink); }
  .divider { position: absolute; left: 166px; width: 475px; height: 1px; background: var(--line); }

  .power-option { position: absolute; left: 166px; display: flex; align-items: center; height: 26px; }
  .radio { width: 26px; height: 26px; border-radius: 50%; border: 1px solid var(--blue); margin-right: 13px; flex: none; display: flex; align-items: center; justify-content: center; }
  .radio.checked { background: var(--green); border-color: var(--green); }
  .option-label { font-size: 15px; letter-spacing: 0.4px; }
  .option-label strong { font-weight: 700; }
</style>
</head>
<body>
<main class="order-card">
  <header class="card-header">
    <h1 class="page-title">Calculate Your Order</h1>
    <aside class="help-center">
      <div class="help-heading">
        <svg width="17" height="17" viewBox="0 0 17 17" aria-hidden="true"><circle cx="8.5" cy="8.5" r="8.5" fill="#1e7be0"/><text x="8.5" y="13" text-anchor="middle" font-family="Open Sans, sans-serif" font-weight="700" font-size="12" fill="#fff">?</text></svg>
        HELP CENTER
      </div>
      <p class="help-text">If you need assistance while calculating your order, contact us by phone or email below:</p>
      <p class="help-contact">+12 555 01234 / help@quotedesk.com</p>
    </aside>
  </header>

  <section class="step" style="top:0">
    <div class="step-number" style="top:166px">1</div>
    <h2 class="step-title" style="top:166px">Duration</h2>
    <p class="step-desc" style="top:198px">Lorem ipsum dolor sit amet, consectetur adipiscing elit.</p>
    <div class="stepper" style="top:230px">
      <button class="step-btn minus" style="left:227px">-12</button>
      <button class="step-btn minus" style="left:270px">-1</button>
      <div class="value-pill"><span class="value-number">24</span><span class="value-unit">Months</span></div>
      <button class="step-btn plus" style="left:499px">+1</button>
      <button class="step-btn plus" style="left:542px">+12</button>
    </div>
    <div class="divider" style="top:309px"></div>
  </section>

  <section class="step" style="top:0">
    <div class="step-number" style="top:336px">2</div>
    <h2 class="step-title" style="top:337px">Count</h2>
    <p class="step-desc" style="top:369px">Sed finibus sit amet arcu quis ultricies.</p>
    <div class="stepper" style="top:401px">
      <button class="step-btn minus" style="left:227px">-10</button>
      <button class="step-btn minus" style="left:270px">-1</button>
      <div class="value-pill"><span class="value-number">100</span><span class="value-unit">Items</span></div>
      <button class="step-btn plus" style="left:499px">+1</button>
      <button class="step-btn plus" style="left:542px">+10</button>
    </div>
    <div class="divider" style="top:480px"></div>
  </section>

  <section class="step" style="top:0">
    <div class="step-number" style="top:531px">3</div>
    <h2 class="step-title" style="top:531px">Engine Power</h2>
    <p class="step-desc" style="top:563px">Nam rutrum, sapien et ornare viverra, leo mi rhoncus ipsum lorem arcu a est.</p>
    <div class="power-option" style="top:595px"><span class="radio"></span><span class="option-label"><strong>$360/year -</strong> Bronze Power</span></div>
    <div class="power-option" style="top:630px"><span class="radio"></span><span class="option-label"><strong>$600/year -</strong> Silver Power</span></div>
    <div class="power-option" style="top:665px"><span class="radio checked"><svg width="14" height="11" viewBox="0 0 14 11" aria-hidden="true"><path d="M1.5 5.5 L5 9 L12.5 1.5" fill="none" stroke="#fff" stroke-width="1.8"/></svg></span><span class="option-label"><strong>$1m/year -</strong> Gold Power</span></div>
    <div class="power-option" style="top:700px"><span class="radio"></span><span class="option-label"><strong>$3m/year -</strong> Platinum Power</span></div>
    <div class="divider" style="top:767px"></div>
  </section>
</main>
</body>
</html>
```